Copper Lantern Vapors - Premium labels

Copper Lantern Vapors is a business that has multiple retail locations where we sell e-cigs and liquid for e-cigs. We have our own house line of liquid but we're looking for expand our business with a premium brand of liquid. This label would be for our premium liquid bottles. We'd like to go with a Four Horseman of the Apocalypse theme. So I'm thinking we would have 4 flavors named White, Black, Red, and Pale.

Example label template attached.

Please let me know if you have any questions!

Thanks
(attaching our standard logo as reference)

Industry/Entity Type

Business

Requirements
Must have
• The branding should be for the Four Horseman theme. We want this to seem like it's own brand. Should have four different variations of labels - one each for White, Black, Red, and Pale. They can be very similar (or different), no preference at the moment.

```html
<!DOCTYPE html>
<html lang="en">
<head>
<meta charset="utf-8">
<title>Copper Lantern Vapors – Premium Labels</title>
<link rel="stylesheet" href="https://fonts.googleapis.com/css2?family=Audiowide&family=Cinzel:wght@500&family=Tinos&display=swap">
<style>
  :root {
    --page-bg: #ececec;
    --label-black: #0b0b0b;
    --strip-white: #f2f2f2;
    --strip-text: #2a2a2a;
    --brand-blue: #2f9ddb;
    --ground: #050505;
    --moon-black: #6e6e6e;
    --moon-pale: #f1e6bd;
    --moon-white: #f4f4f2;
    --moon-red: #d3222a;
    --title-black: #8a8a8a;
    --title-pale: #f3e6b8;
    --title-white: #ffffff;
    --title-red: #d8252c;
  }
  * { box-sizing: border-box; margin: 0; padding: 0; }
  html, body { width: 1200px; height: 1200px; overflow: hidden; }
  body {
    background: radial-gradient(circle at 50% 40%, #fafafa 0%, var(--page-bg) 75%);
    display: flex;
    align-items: center;
    justify-content: center;
  }
  .label-set {
    display: flex;
    gap: 22px;
  }
  .label {
    width: 268px;
    height: 620px;
    display: grid;
    grid-template-columns: 38px 1fr 34px;
    box-shadow: 0 10px 30px rgba(0,0,0,0.18);
  }
  .strip {
    background: var(--strip-white);
    color: var(--strip-text);
    font-family: "Tinos", serif;
    font-size: 9px;
    line-height: 1.25;
    display: flex;
    align-items: center;
    justify-content: center;
    padding: 14px 4px;
  }
  .strip-ingredients p {
    writing-mode: vertical-rl;
    transform: rotate(180deg);
    max-height: 480px;
  }
  .strip-ingredients b { font-weight: 700; }
  .strip-warning p {
    writing-mode: vertical-rl;
    font-size: 10px;
    border: 1px solid #555;
    padding: 6px 2px;
  }
  .panel {
    background: var(--label-black);
    display: flex;
    flex-direction: column;
    align-items: center;
    padding-top: 56px;
  }
  .brand {
    display: flex;
    align-items: center;
    gap: 8px;
    color: var(--brand-blue);
    font-family: "Audiowide", sans-serif;
    font-size: 15px;
    line-height: 1.15;
    text-transform: uppercase;
  }
  .brand-dot {
    width: 22px;
    height: 22px;
    border-radius: 50%;
    background: var(--brand-blue);
    flex: none;
  }
  .scene {
    position: relative;
    width: 100%;
    height: 260px;
    margin-top: 40px;
  }
  .moon {
    position: absolute;
    left: 50%;
    top: 0;
    width: 176px;
    height: 176px;
    margin-left: -88px;
    border-radius: 50%;
  }
  .ground {
    position: absolute;
    left: 0; right: 0; bottom: 0;
    height: 96px;
    background: var(--ground);
    border-radius: 50% 50% 0 0 / 28px 28px 0 0;
  }
  .title {
    margin-top: 14px;
    font-family: "Cinzel", serif;
    font-weight: 500;
    font-size: 34px;
    letter-spacing: 0.28em;
    padding-left: 0.28em;
  }
  .label-black .moon { background: radial-gradient(circle at 40% 40%, #8a8a8a, var(--moon-black)); }
  .label-black .title { color: var(--title-black); }
  .label-pale .moon { background: radial-gradient(circle at 40% 40%, #fbf3d6, var(--moon-pale)); }
  .label-pale .title { color: var(--title-pale); }
  .label-white .moon { background: radial-gradient(circle at 40% 40%, #ffffff, var(--moon-white) 60%, #dcdcdc); }
  .label-white .title { color: var(--title-white); }
  .label-red .moon { background: radial-gradient(circle at 40% 40%, #e33a3f, var(--moon-red)); }
  .label-red .title { color: var(--title-red); }
</style>
</head>
<body>
  <main class="label-set">

    <article class="label label-black">
      <aside class="strip strip-ingredients"><p><b>Ingredients:</b> USP Grade Glycerin, USP Grade Propylene Glycol, Natural &amp; Artificial Flavoring, USP Grade Nicotine. <b>Prop 65</b> Warning: Keep out of reach of children and pets. 60ML 70/30</p></aside>
      <section class="panel">
        <div class="brand"><span class="brand-dot"></span><span>Copper Lantern<br>Vapors</span></div>
        <div class="scene" role="img" aria-label="Grey moon with a horseman silhouette holding scales beside a bare tree on a grassy hill">
          <div class="moon"></div>
          <div class="ground"></div>
        </div>
        <h2 class="title">BLACK</h2>
      </section>
      <aside class="strip strip-warning"><p>WARNING: This product contains nicotine.</p></aside>
    </article>

    <article class="label label-pale">
      <aside class="strip strip-ingredients"><p><b>Ingredients:</b> USP Grade Glycerin, USP Grade Propylene Glycol, Natural &amp; Artificial Flavoring, USP Grade Nicotine. <b>Prop 65</b> Warning: Keep out of reach of children and pets. 60ML 70/30</p></aside>
      <section class="panel">
        <div class="brand"><span class="brand-dot"></span><span>Copper Lantern<br>Vapors</span></div>
        <div class="scene" role="img" aria-label="Pale cream moon with a hooded rider carrying a scythe beside a twisted bare tree">
          <div class="moon"></div>
          <div class="ground"></div>
        </div>
        <h2 class="title">PALE</h2>
      </section>
      <aside class="strip strip-warning"><p>WARNING: This product contains nicotine.</p></aside>
    </article>

    <article class="label label-white">
      <aside class="strip strip-ingredients"><p><b>Ingredients:</b> USP Grade Glycerin, USP Grade Propylene Glycol, Natural &amp; Artificial Flavoring, USP Grade Nicotine. <b>Prop 65</b> Warning: Keep out of reach of children and pets. 60ML 70/30</p></aside>
      <section class="panel">
        <div class="brand"><span class="brand-dot"></span><span>Copper Lantern<br>Vapors</span></div>
        <div class="scene" role="img" aria-label="White moon with a rider raising a sword in front of a gnarled bare tree">
          <div class="moon"></div>
          <div class="ground"></div>
        </div>
        <h2 class="title">WHITE</h2>
      </section>
      <aside class="strip strip-warning"><p>WARNING: This product contains nicotine.</p></aside>
    </article>

    <article class="label label-red">
      <aside class="strip strip-ingredients"><p><b>Ingredients:</b> USP Grade Glycerin, USP Grade Propylene Glycol, Natural &amp; Artificial Flavoring, USP Grade Nicotine. <b>Prop 65</b> Warning: Keep out of reach of children and pets. 60ML 70/30</p></aside>
      <section class="panel">
        <div class="brand"><span class="brand-dot"></span><span>Copper Lantern<br>Vapors</span></div>
        <div class="scene" role="img" aria-label="Red moon with a galloping archer on horseback beside a bare tree">
          <div class="moon"></div>
          <div class="ground"></div>
        </div>
        <h2 class="title">RED</h2>
      </section>
      <aside class="strip strip-warning"><p>WARNING: This product contains nicotine.</p></aside>
    </article>

  </main>
</body>
</html>
```